Business Card Design for drone videography and photography

I have a Vexor Talon 3 drone. I am looking for a logo to somehow incorporate with my business name. I don't even know what is an appropriate font. I am most filming real estate homes. I want something simplistic and a logo that makes sense for the business that I'm in. xxxxxxxxxxxxxxxxxxxxxxxxxxxxxxxxxxxxxxxxxxxxxxxxxxxxxxxxxxxxxxxxxxxxxxxxxxxxxxxxxxxxxxxxxxxxxxxxxxxxxxxxxxxxxxxxxxxxxxxxxxxxxxxxxxxxxxxxxxxxxxxxxxxxxxxxxxxxxxxxxxxxxxxxxxxxxxxxxxxxxxxxxxxxxxxxxxxxxxxxxxxxxxxxxxxxxxxxxxxxxxxxxxxxxxxxxxxxxxxxxxxxxxxxxxxxxxxxxxxxxxxxxxxxxxxxxxxxxxxxxxxxxxxxxxxxxxxxxxxxxxxxxxxxxxxxxxxxxxxxxxxxxxxxxxxxxxxxxxxxxxxxxxxxxxxxxxxxxxxxxxxxxxxxxxxxxxxxxxxxxxxxxxxxxxxxxxxxxxxxxxxxxxxxxxxxxxxxxxxxxxxxxxxxxxxxxxxxxxxxxxxxxxxxxxxxxxxxxxxxxxxxxxxxxxxxxxxxxxxxxxxxxxxxxxxxxxxxxxxxxxxxxxxxxxxxxxxxxxxxxxxxxxxxxxxxxxxxxxxxxxxxxxxxxxxxxxxxxxxxxxxxxxxxxxxxxxxxxxxxxxxxxxxxxxxxxxxxxxxxxxxxxxxxxxxxxxxxxxxxxxxxxxxxxxxxxxxxxxxxxxxxxxxxxxxxxxxxxxxxxxxxxxxxxxxxxxxxxxxxxxxxxxxxxxxxxxxxxxxxxxxxxxxxxxxxxxxxxxxxxxxxxxxxxxxxxxxxxxxxxxxxxxxxxxxxxxxxxxxxxxxxxxxxxxxxxxxxxxxxxxxxxxxxxxxxxxxxxxxxxxxxxxxxxxxxxxxxxxxxxxxxxxxxxxxxxxxxxxxxxxxxxxxxxxxxxxxxxxxxxxxxxxxxxxxxxxxxxxxxxxxxxxxxxxxxxxxxxxxxxxxxxxxxxxxxxxxxxxxxxxxxxxxxxxxxxxxxxxxxxxxxxxxxxxxxxxxxxxxxxxxxxxxxxxxxxxxxxxxxxxxxxxxxxxxxxxxxxxxxxxxxxxxxxxxxxxxxxxxxxxxxxxxxxxxxxxxxxxxx

Target Market(s)

Real estate

Industry/Entity Type

Business

Contact Information for Business Card

BRANDT SKYVIEW STUDIO
Daniel Brandt
Owner/Operator

48305 Birch Way
Fernhollow MO 63999

314-720-4163
dbrandt@brandtskyviewstudio.example

NCQ Drone Certified
Insured
Section 333 Exempt
Halvo Wing Class Certified

Font styles to use
Other font styles liked:
• PUMP DEMI BOLD LET

Requirements
Must have
• Maybe have the certifications on the back??? The business card must be more serious than playful
Nice to have
• Possibly have the logo work itself into the business name?
Should not have
• nothing that looks like a "fun" business. I want this business card to look professional but also simplistic. I don't want a picture that I took from my drone as the background.

```html
<!DOCTYPE html>
<html lang="en">
<head>
<meta charset="utf-8">
<title>Brandt Skyview Studio: Business Card Options</title>
<link rel="stylesheet" href="https://fonts.googleapis.com/css2?family=Lora:wght@400;700&family=Open+Sans:wght@300;400;600&display=swap">
<style>
  :root {
    --sheet: #ececec;
    --card-light: #ffffff;
    --card-dark: #474747;
    --accent-blue: #4a9fd8;
    --ink-grey: #6e6e6e;
    --ink-soft: #8c8c8c;
    --ink-light: #d6d6d6;
    --wordmark-soft: #a3a3a3;
    --wordmark-dark: #5f5f5f;
    --wordmark-white: #ececec;
    --label: #1a1a1a;
  }
  * { margin: 0; padding: 0; box-sizing: border-box; }
  html, body {
    width: 1200px; height: 465px; overflow: hidden;
    background: var(--sheet);
  }
  .sheet { position: relative; width: 1200px; height: 465px; }

  .option-label {
    position: absolute; width: 270px; text-align: center;
    font: 700 12px "Lora", serif; color: var(--label);
  }
  .option-label.top { top: 41px; }
  .option-label.bottom { top: 429px; }

  .card {
    position: absolute; width: 270px; height: 168px; overflow: hidden;
    font-family: "Open Sans", sans-serif;
  }
  .card.light { background: var(--card-light); top: 62px; }
  .card.dark { background: var(--card-dark); top: 246px; }
  .col-1 { left: 26px; }
  .col-2 { left: 318px; }
  .col-3 { left: 603px; }
  .col-4 { left: 906px; }

  .identity { position: absolute; top: 42px; }
  .identity.right { right: 36px; text-align: right; }
  .identity.left { left: 34px; text-align: left; }
  .person-name {
    font: 400 14px/1.1 "Lora", serif; color: var(--accent-blue);
  }
  .person-role {
    font: 300 8px/1.3 "Open Sans", sans-serif; color: var(--ink-soft);
  }
  .dark .person-role { color: var(--ink-light); }

  .contact { position: absolute; color: var(--ink-grey); white-space: nowrap; }
  .dark .contact { color: var(--ink-light); }
  .contact.left { left: 35px; top: 76px; }
  .contact.right { left: 131px; top: 74px; }
  .phone { font-size: 7px; line-height: 1.3; }
  .details { font-size: 5.2px; line-height: 1.25; }
  .credentials { font-size: 5.2px; line-height: 1.2; margin-top: 9px; }

  .wordmark {
    position: absolute; left: 0; right: 0; top: 78px; text-align: center;
    font: 600 13px "Open Sans", sans-serif; letter-spacing: 0.1px;
  }
  .light .wordmark.soft { color: var(--wordmark-soft); }
  .light .wordmark.strong { color: var(--wordmark-dark); }
  .dark .wordmark.strong { color: var(--wordmark-white); }
  .dark .wordmark.soft { color: var(--wordmark-soft); }
</style>
</head>
<body>
<main class="sheet">
  <div class="option-label top" style="left:26px">1-1</div>
  <div class="option-label top" style="left:318px">1-2</div>
  <div class="option-label top" style="left:603px">2-1</div>
  <div class="option-label top" style="left:906px">2-2</div>

  <section class="card light col-1">
    <div class="identity right">
      <div class="person-name">Daniel Brandt</div>
      <div class="person-role">Owner/Operator</div>
    </div>
    <div class="contact left">
      <div class="phone">314-720-4163</div>
      <div class="details">dbrandt@brandtskyviewstudio.example<br>48305 Birch Way Fernhollow MO 63999</div>
      <div class="credentials">NCQ Drone Certified<br>Insured<br>Section 333 Exempt<br>Halvo Wing Class Certified</div>
    </div>
  </section>
  <section class="card light col-2">
    <div class="wordmark soft">Brandt Skyview Studio</div>
  </section>

  <section class="card light col-3">
    <div class="identity left">
      <div class="person-name">Daniel Brandt</div>
      <div class="person-role">Owner/Operator</div>
    </div>
    <div class="contact right">
      <div class="phone">314-720-4163</div>
      <div class="details">dbrandt@brandtskyviewstudio.example<br>48305 Birch Way Fernhollow MO 63999</div>
      <div class="credentials">NCQ Drone Certified<br>Insured<br>Section 333 Exempt<br>Halvo Wing Class Certified</div>
    </div>
  </section>
  <section class="card light col-4">
    <div class="wordmark strong">Brandt Skyview Studio</div>
  </section>

  <section class="card dark col-1">
    <div class="identity right">
      <div class="person-name">Daniel Brandt</div>
      <div class="person-role">Owner/Operator</div>
    </div>
    <div class="contact left">
      <div class="phone">314-720-4163</div>
      <div class="details">dbrandt@brandtskyviewstudio.example<br>48305 Birch Way Fernhollow MO 63999</div>
      <div class="credentials">NCQ Drone Certified<br>Insured<br>Section 333 Exempt<br>Halvo Wing Class Certified</div>
    </div>
  </section>
  <section class="card dark col-2">
    <div class="wordmark strong">Brandt Skyview Studio</div>
  </section>

  <section class="card dark col-3">
    <div class="identity left">
      <div class="person-name">Daniel Brandt</div>
      <div class="person-role">Owner/Operator</div>
    </div>
    <div class="contact right">
      <div class="phone">314-720-4163</div>
      <div class="details">dbrandt@brandtskyviewstudio.example<br>48305 Birch Way Fernhollow MO 63999</div>
      <div class="credentials">NCQ Drone Certified<br>Insured<br>Section 333 Exempt<br>Halvo Wing Class Certified</div>
    </div>
  </section>
  <section class="card dark col-4">
    <div class="wordmark soft">Brandt Skyview Studio</div>
  </section>

  <div class="option-label bottom" style="left:26px">3-1</div>
  <div class="option-label bottom" style="left:318px">3-2</div>
  <div class="option-label bottom" style="left:603px">4-1</div>
  <div class="option-label bottom" style="left:906px">4-2</div>
</main>
</body>
</html>
```